Tolland Imaging
Mobile Ultrasound Solutions
Professional
Helen Marsh
Executive Sales Representative
Fenwick Bay, Oregon
info@tollandimaging-example.com
tollandimaging-example.com

```html
<!DOCTYPE html>
<html lang="en">
<head>
<meta charset="utf-8">
<title>Tolland Imaging Business Card</title>
<link href="https://fonts.googleapis.com/css2?family=Arimo:wght@400;700&display=swap" rel="stylesheet">
<style>
  :root {
    --stage: #e9e6e1;
    --card: #ffffff;
    --card-edge: #f1f3f6;
    --brand-blue: #2a49b8;
    --accent-blue: #1f6fd0;
    --text-grey: #4a4d55;
    --link-blue: #2a49b8;
  }
  * { margin: 0; padding: 0; box-sizing: border-box; }
  html, body {
    width: 1200px; height: 1028px; overflow: hidden;
    background: var(--stage);
    font-family: "Arimo", Arial, sans-serif;
  }
  .canvas { position: relative; width: 1200px; height: 1028px; }
  .card {
    position: absolute; width: 590px; height: 340px;
    background: linear-gradient(180deg, var(--card) 60%, var(--card-edge) 100%);
    border-radius: 18px;
    box-shadow: 0 10px 24px rgba(0,0,0,0.22);
  }
  .card-front { left: 145px; top: 165px; }
  .card-back { left: 450px; top: 470px; }

  .brand { display: flex; align-items: center; gap: 12px; }
  .brand-dot { border-radius: 50%; background: var(--brand-blue); flex: none; }
  .brand-name { color: var(--brand-blue); font-weight: 700; white-space: nowrap; }

  .card-front .brand { position: absolute; left: 48px; top: 128px; }
  .card-front .brand-dot { width: 22px; height: 22px; }
  .card-front .brand-name { font-size: 34px; }

  .contact-bar {
    position: absolute; left: 0; top: 225px; width: 20px; height: 56px;
    background: linear-gradient(180deg, var(--accent-blue), var(--brand-blue));
  }
  .contact { position: absolute; left: 48px; top: 226px; font-size: 13.5px; line-height: 17px; color: var(--text-grey); }
  .website { position: absolute; left: 48px; top: 296px; font-size: 13.5px; color: var(--link-blue); }

  .person { position: absolute; left: 336px; top: 223px; }
  .person-name { font-size: 22px; font-weight: 700; color: var(--brand-blue); }
  .person-title { font-size: 14px; color: var(--text-grey); margin-top: 3px; }

  .card-back .brand { position: absolute; right: 44px; top: 232px; gap: 8px; }
  .card-back .brand-dot { width: 14px; height: 14px; }
  .card-back .brand-name { font-size: 18px; }
  .card-back .website { left: auto; right: 44px; top: 268px; font-size: 13px; }
</style>
</head>
<body>
<main class="canvas">
  <section class="card card-front" aria-label="Business card front">
    <div class="brand">
      <span class="brand-dot"></span>
      <span class="brand-name">Tolland Imaging</span>
    </div>
    <div class="contact-bar"></div>
    <div class="contact">
      <p>Fenwick Bay, Oregon</p>
      <p>Phone: 555-010-4821</p>
      <p>Email: info@tollandimaging-example.com</p>
    </div>
    <p class="website">www.tollandimaging-example.com</p>
    <div class="person">
      <p class="person-name">Helen Marsh</p>
      <p class="person-title">Executive Sales Representative</p>
    </div>
  </section>

  <section class="card card-back" aria-label="Business card back">
    <div class="brand">
      <span class="brand-dot"></span>
      <span class="brand-name">Tolland Imaging</span>
    </div>
    <p class="website">www.tollandimaging-example.com</p>
  </section>
</main>
</body>
</html>
```